Business card design needed for a security services business.

We provide a wide range of security services from guard personnel to electronic systems.

Industry/Entity Type

Security Industry

Contact Information for Business Card

Brent Holloway, Owner Office: 780.555.0148; Cell: 780.555.0193 Email: brent@norcrestwatchgroup.example; Address 20487 163 St Edmonton, AB T5X 2K8

Colors
0054AA
0677BA
7BADD7
CADEEF
E8F1F8

Requirements
Nice to have
• On the back of the card I would like to possible list the services I provide: Guards Mobiles Live Video Surveillance Access Intrusion

```html
<!DOCTYPE html>
<html lang="en">
<head>
<meta charset="utf-8">
<title>Norcrest Watch Group – Business Card</title>
<link href="https://fonts.googleapis.com/css2?family=Open+Sans:wght@400;600;700&display=swap" rel="stylesheet">
<style>
  :root {
    --stage: #3b3b3b;
    --paper: #ffffff;
    --brand-blue: #0677ba;
    --deep-blue: #0054aa;
    --ink: #4a4a4a;
    --muted: #6b6b6b;
    --back-dark: #0d0d0d;
    --back-mid: #1e1e1e;
  }
  * { box-sizing: border-box; margin: 0; padding: 0; }
  html, body {
    width: 1200px; height: 801px; overflow: hidden;
    background: var(--stage);
    font-family: "Open Sans", Arial, sans-serif;
  }
  .stage {
    position: relative; width: 1200px; height: 801px;
    display: flex; align-items: center; justify-content: center; gap: 60px;
  }
  .card {
    position: relative; width: 525px; height: 300px;
    border-bottom: 3px solid var(--brand-blue);
    box-shadow: 0 14px 30px rgba(0,0,0,.35);
    overflow: hidden;
  }
  .card--front { background: var(--paper); }
  .brand {
    position: absolute; top: 38px; right: 40px; text-align: right;
  }
  .brand__name {
    font-weight: 700; font-size: 24px; letter-spacing: .5px;
    color: var(--brand-blue); text-transform: uppercase; line-height: 1.1;
  }
  .brand__rule { height: 1px; background: var(--muted); margin: 6px 0 4px; }
  .brand__sub {
    font-size: 11px; letter-spacing: 6px; color: var(--brand-blue);
    text-transform: uppercase;
  }
  .divider {
    position: absolute; left: 28px; right: 40px; top: 136px;
    height: 1px; background: var(--brand-blue);
  }
  .address {
    position: absolute; right: 40px; top: 150px; text-align: right;
    font-size: 12px; color: var(--ink); line-height: 1.45;
  }
  .person { position: absolute; left: 28px; top: 156px; }
  .person__name {
    font-weight: 700; font-size: 20px; color: var(--brand-blue);
    text-transform: uppercase; letter-spacing: .3px;
  }
  .person__role { font-size: 13px; color: var(--muted); margin-bottom: 8px; }
  .contacts { list-style: none; }
  .contacts li {
    display: flex; align-items: center; gap: 8px;
    font-size: 13px; color: var(--ink); line-height: 1.45;
  }
  .contacts svg { width: 11px; height: 11px; fill: var(--brand-blue); flex: none; }
  .card--back {
    background: var(--back-dark);
    display: flex; align-items: center; justify-content: flex-end;
  }
  .back-texture {
    position: absolute; inset: 0;
    background: linear-gradient(120deg, var(--back-dark) 0%, var(--back-mid) 55%, #2a2a2a 100%);
  }
  .back-mark {
    position: relative; margin: 90px 50px 0 0;
    font-weight: 700; font-size: 26px; letter-spacing: 1px;
    color: var(--paper); text-transform: uppercase;
  }
</style>
</head>
<body>
<main class="stage">
  <section class="card card--front" aria-label="Card front">
    <div class="brand">
      <div class="brand__name">Norcrest Watch</div>
      <div class="brand__rule"></div>
      <div class="brand__sub">Group</div>
    </div>
    <div class="divider"></div>
    <address class="address">20487 163 St Edmonton<br>AB T5X 2K8</address>
    <div class="person">
      <h1 class="person__name">Brent Holloway</h1>
      <p class="person__role">Owner</p>
      <ul class="contacts">
        <li><svg viewBox="0 0 24 24"><path d="M6.6 10.8a15 15 0 0 0 6.6 6.6l2.2-2.2c.3-.3.7-.4 1-.2 1.1.4 2.3.6 3.6.6.6 0 1 .4 1 1V20c0 .6-.4 1-1 1A17 17 0 0 1 3 4c0-.6.4-1 1-1h3.5c.6 0 1 .4 1 1 0 1.3.2 2.5.6 3.6.1.3 0 .7-.2 1z"/></svg>780.555.0148</li>
        <li><svg viewBox="0 0 24 24"><path d="M7 1h10a2 2 0 0 1 2 2v18a2 2 0 0 1-2 2H7a2 2 0 0 1-2-2V3a2 2 0 0 1 2-2zm0 3v14h10V4zm5 15.5a1 1 0 1 0 0 2 1 1 0 0 0 0-2z"/></svg>780.555.0193</li>
        <li><svg viewBox="0 0 24 24"><path d="M2 5h20v14H2zm2 2v.5l8 5 8-5V7zm0 2.8V17h16V9.8l-8 5z"/></svg>brent@norcrestwatchgroup.example</li>
        <li><svg viewBox="0 0 24 24"><path d="M12 2a10 10 0 1 0 0 20 10 10 0 0 0 0-20zm0 2c1 0 2.3 2 2.8 5H9.2C9.7 6 11 4 12 4zM4.3 11h4.7a18 18 0 0 0 0 2H4.3a8 8 0 0 1 0-2zm6.7 0h2a16 16 0 0 1 0 2h-2a16 16 0 0 1 0-2zm4 0h4.7a8 8 0 0 1 0 2H15a18 18 0 0 0 0-2zm-5.8 4h5.6c-.5 3-1.8 5-2.8 5s-2.3-2-2.8-5z"/></svg>www.norcrestwatchgroup.example</li>
      </ul>
    </div>
  </section>

  <section class="card card--back" aria-label="Card back">
    <div class="back-texture" role="img" aria-label="Repeating glossy dark brand-initial texture across the card back"></div>
    <div class="back-mark">Norcrest</div>
  </section>
</main>
</body>
</html>
```